Business Card Design Project

Dunmore Freightwerk is an IT focussed, forward thinking online uniform and inventory management company supplying into large scale Defence, Emergency Services and Government Department contracts.

Our logo is our name, however we have adopted the use of a globe (see attached) within a recent promotional DVD and would like this worked into the design.

We are wanting something sharp and sophisticated.

Requirements
Must have
• Space for QR Code
Website details www.dunmorefreightwerk.example
Nice to have
• 2 sided - name/logo only on rear side.

```html
<!DOCTYPE html>
<html lang="en">
<head>
<meta charset="utf-8">
<title>Dunmore Freightwerk — Business Card</title>
<link rel="stylesheet" href="https://fonts.googleapis.com/css2?family=Tinos&family=PT+Sans&family=Open+Sans:wght@700&display=swap">
<style>
  :root {
    --stage: #000000;
    --page: #ffffff;
    --front-green: #95c13d;
    --back-grey: #c8c8c6;
    --ink-white: #ffffff;
    --ink-dark: #1a1a1a;
    --mark-dark: #4f6a1c;
    --mark-grey: #8f8f8f;
    --dot-blue: rgba(150, 178, 205, 0.55);
  }
  html, body {
    margin: 0;
    padding: 0;
    width: 1200px;
    height: 557px;
    overflow: hidden;
    background: var(--page);
  }
  .stage {
    position: relative;
    width: 1200px;
    height: 557px;
    background: var(--stage);
    border-radius: 16px;
    overflow: hidden;
  }
  .card {
    position: absolute;
    border-radius: 24px;
    overflow: hidden;
  }
  .card--front {
    left: 69px; top: 133px; width: 517px; height: 295px;
    background: var(--front-green);
  }
  .card--back {
    left: 616px; top: 128px; width: 523px; height: 297px;
    background: var(--back-grey);
  }
  .halftone {
    position: absolute;
  }
  .card--front .halftone {
    left: 0; top: 0; width: 190px; height: 295px;
    background: linear-gradient(90deg, rgba(160,190,200,0.55) 0%, rgba(160,190,200,0.25) 55%, rgba(149,193,61,0) 100%);
  }
  .card--back .halftone {
    left: 0; top: 50px; width: 190px; height: 247px;
    background: linear-gradient(90deg, var(--dot-blue) 0%, rgba(150,178,205,0.25) 60%, rgba(200,200,198,0) 100%);
  }
  .wordmark {
    position: absolute;
    margin: 0;
    font-family: "Tinos", "Times New Roman", serif;
    font-weight: 400;
    color: var(--ink-white);
    white-space: nowrap;
    line-height: 1;
  }
  .card--front .wordmark {
    left: 0; width: 517px; top: 74px;
    text-align: center;
    font-size: 35px;
  }
  .card--back .wordmark {
    left: 17px; top: 30px;
    font-size: 16px;
  }
  .mark-circle {
    position: absolute;
    border-radius: 50%;
  }
  .card--front .mark-circle {
    left: 205px; top: 118px; width: 88px; height: 88px;
    background: var(--mark-dark);
  }
  .card--back .mark-circle {
    left: 86px; top: 56px; width: 62px; height: 62px;
    background: var(--mark-grey);
  }
  .website {
    position: absolute;
    left: 0; width: 517px; top: 266px;
    text-align: center;
    font-family: "PT Sans", Arial, sans-serif;
    font-size: 14px;
    letter-spacing: 4.2px;
    color: var(--ink-white);
  }
  .contact-list {
    position: absolute;
    left: 227px; top: 194px;
    margin: 0; padding: 0;
    list-style: none;
    font-family: "PT Sans", Arial, sans-serif;
    font-size: 12.5px;
    color: var(--ink-dark);
  }
  .contact-item {
    display: flex;
    align-items: center;
    height: 18px;
    margin-bottom: 9px;
  }
  .contact-icon {
    width: 18px; height: 18px;
    margin-right: 10px;
    flex: none;
    fill: var(--ink-dark);
  }
  .side-label {
    position: absolute;
    top: 484px;
    width: 300px;
    text-align: center;
    font-family: "Open Sans", Arial, sans-serif;
    font-weight: 700;
    font-size: 25px;
    color: var(--ink-white);
  }
  .side-label--front { left: 166px; }
  .side-label--back { left: 779px; }
</style>
</head>
<body>
<main class="stage">
  <section class="card card--front">
    <div class="halftone" role="img" aria-label="Soft halftone dot pattern fading across the left of the card"></div>
    <h1 class="wordmark">DUNMORE FREIGHTWERK</h1>
    <div class="mark-circle"></div>
    <p class="website" style="margin:0">www.dunmorefreightwerk.example</p>
  </section>

  <section class="card card--back">
    <div class="halftone" role="img" aria-label="Soft halftone dot pattern fading across the left of the card"></div>
    <h2 class="wordmark">DUNMORE FREIGHTWERK</h2>
    <div class="mark-circle"></div>
    <ul class="contact-list">
      <li class="contact-item">
        <svg class="contact-icon" viewBox="0 0 18 18" aria-hidden="true"><path d="M9 1 L17 8 L15 8 L15 17 L11 17 L11 12 L7 12 L7 17 L3 17 L3 8 L1 8 Z"/></svg>
        <span>Sydney &amp; Melbourne</span>
      </li>
      <li class="contact-item">
        <svg class="contact-icon" viewBox="0 0 18 18" aria-hidden="true"><path d="M4 1 L7 5 L5.5 7 C6.5 9.5 8.5 11.5 11 12.5 L13 11 L17 14 L15 17 C8 17 1 10 1 3 Z"/></svg>
        <span>+61 2 5550 1234 | Fax +61 2 5550 1235</span>
      </li>
      <li class="contact-item">
        <svg class="contact-icon" viewBox="0 0 18 18" aria-hidden="true"><path d="M1 4 H17 V15 H1 Z M2.5 5 L9 10 L15.5 5 Z" fill-rule="evenodd"/></svg>
        <span>r.hale@dunmorefreightwerk.example</span>
      </li>
    </ul>
  </section>

  <p class="side-label side-label--front" style="margin:0">Front Side</p>
  <p class="side-label side-label--back" style="margin:0">Back Side</p>
</main>
</body>
</html>
```